One Page Sales Flyer for Wireless Survey- Computer Hardware

I want a designer to create a one page 4 color sales slick to be given to our sales team to sell to the end customers. I would like a visual picture of a heat map so zavvix "heat map wireless" to get an idea of how that image should look.

```html
<!DOCTYPE html>
<html lang="en">
<head>
<meta charset="utf-8">
<title>Trestle – Wireless Site Survey Sales Flyer</title>
<link href="https://fonts.googleapis.com/css2?family=Roboto+Condensed:wght@400;700&display=swap" rel="stylesheet">
<style>
  :root {
    --canvas: #f2f2f2;
    --paper-grey: #e6e5e6;
    --heat-red: #dc4a48;
    --heat-orange: #e27d4e;
    --heat-amber: #eab45c;
    --heat-yellow: #f0e35c;
    --heat-green: #b8d35a;
    --brand-blue: #3f9bd6;
    --ink: #2e2e2e;
    --white: #ffffff;
    --logo-grey: #3a3a3a;
  }
  * { box-sizing: border-box; margin: 0; padding: 0; }
  html, body { width: 1200px; height: 1200px; overflow: hidden; }
  body {
    background: var(--canvas);
    font-family: "Roboto Condensed", "Arial Narrow", sans-serif;
    color: var(--ink);
  }
  .flyer {
    position: absolute;
    left: 186px; top: 20px;
    width: 828px; height: 1160px;
    background: var(--paper-grey);
    overflow: hidden;
  }
  .heat-map { position: absolute; inset: 0; width: 100%; height: 100%; }

  .brand {
    position: absolute; left: 660px; top: 35px; width: 120px;
    display: flex; flex-direction: column; align-items: center; gap: 10px;
  }
  .brand-mark { width: 56px; height: 56px; background: var(--brand-blue); border-radius: 6px; }
  .brand-name { font-size: 26px; font-weight: 400; letter-spacing: 1px; color: var(--logo-grey); }

  .headline {
    position: absolute; left: 28px; top: 80px;
    font-size: 41px; line-height: 47px; font-weight: 700;
    color: var(--white);
  }

  .section-tab {
    position: absolute; left: 0; height: 33px;
    background: var(--brand-blue); color: var(--white);
    font-size: 21px; font-weight: 700;
    padding: 3px 0 0 30px;
    border-radius: 0 10px 10px 0;
  }
  .tab-what { top: 265px; width: 283px; }
  .tab-why { top: 538px; width: 414px; }
  .tab-you { top: 805px; width: 270px; }

  .section-body {
    position: absolute; left: 33px; width: 316px;
    font-size: 16.5px; line-height: 23.4px;
    text-align: justify;
  }
  .body-what { top: 316px; }
  .body-why { top: 595px; }

  .reasons {
    position: absolute; left: 30px; top: 861px; width: 620px;
    list-style: none; font-size: 16.5px; line-height: 23px;
  }
  .reasons li { padding-left: 18px; text-indent: -18px; }
  .reasons b { font-weight: 700; }

  .targets-title {
    position: absolute; left: 464px; top: 264px; width: 316px; height: 44px;
    background: var(--brand-blue); color: var(--white);
    border-radius: 8px;
    font-size: 20px; font-weight: 700; text-align: center; line-height: 44px;
  }
  .targets-list {
    position: absolute; left: 464px; top: 319px; width: 316px; height: 364px;
    background: var(--brand-blue); color: var(--white);
    border-radius: 14px;
    list-style: none; text-align: center;
    padding-top: 26px;
    font-size: 20px; line-height: 31px;
  }

  .contact {
    position: absolute; left: 0; top: 1104px; width: 828px;
    text-align: center; font-size: 15px; line-height: 19px;
    padding-left: 150px;
  }
  .contact b { font-weight: 700; }
</style>
</head>
<body>
  <main class="flyer">
    <svg class="heat-map" viewBox="0 0 828 1160" preserveAspectRatio="none" role="img" aria-label="Wireless signal heat map in bands of green, yellow, orange and red">
      <defs>
        <linearGradient id="heatGradient" x1="0" y1="1" x2="1" y2="0">
          <stop offset="0" stop-color="var(--heat-green)"/>
          <stop offset="0.3" stop-color="var(--heat-yellow)"/>
          <stop offset="0.5" stop-color="var(--heat-amber)"/>
          <stop offset="0.7" stop-color="var(--heat-orange)"/>
          <stop offset="0.88" stop-color="var(--heat-red)"/>
        </linearGradient>
      </defs>
      <polygon points="0,0 300,0 440,30 560,60 600,130 630,190 828,205 828,1160 0,1160" fill="url(#heatGradient)"/>
    </svg>

    <div class="brand">
      <span class="brand-mark"></span>
      <span class="brand-name">TRESTLE</span>
    </div>

    <h1 class="headline">Increase Hardware<br>and Services Spend with<br>Wireless Site Surveys</h1>

    <h2 class="section-tab tab-what">What is a wireless site</h2>
    <p class="section-body body-what">A wireless site survey is a compilation of reports showing a visual representation of health of your wireless network. This does not only show how strong or weak a wireless signal is in any location it also helps aid in channel and placement to ensure maximum stable data rates are archived even where the single appears strong.</p>

    <h2 class="section-tab tab-why">Why do customers need a site survey?</h2>
    <p class="section-body body-why">A wireless site survey is a compilation of reports showing a visual representation of health of your wireless network. This does not only show how strong or weak a wireless signal is in any location it also helps aid in channel and placement to ensure maximum stable data rates are archived even where the single appears strong.</p>

    <h2 class="section-tab tab-you">Why should they use you?</h2>
    <ol class="reasons">
      <li><b>1.</b>42% of businesses report some issues with wireless connectivity and acknowledge its effect on the bottom line*</li>
      <li><b>2.</b>Most of these problems are solved through either fine tuning the current equipment (managed services) or purchasing new equipment (incremental sales) of which you can provide both</li>
      <li><b>3.</b>Being a one-stop shop for all your customer's IT needs prevents them from needing additional vendors</li>
      <li><b>4.</b>The increase of IoT (Internet of things) and BYOD (Bring Your Own Device)</li>
    </ol>

    <h2 class="targets-title">TARGET CUSTOMERS</h2>
    <ul class="targets-list">
      <li>Distributors</li>
      <li>Warehouses</li>
      <li>SLED</li>
      <li>K-12</li>
      <li>Medical / Hospitals</li>
      <li>Enterprise F1000</li>
      <li>Sports Venues</li>
      <li>Stadiums</li>
      <li>Hotels</li>
      <li>Retail stores</li>
    </ul>

    <p class="contact"><b>Email:</b> www.yourtrestle.com info@yourtrestle.com<br><b>Telephone:</b> 555-014-2290</p>
  </main>
</body>
</html>
```